Graphic Design Project

We sell organic wines in our store in Paris. When our clients come in the store and buy wines we put the bottle of wine in a plane kraft paper shopping bag.
We'd like now to personalize those shopping bags with our logo of course, but at the same time to give a real personality to those shopping bag, so people who see it might eventually become curious about our store and end up coming in it...
What you have to know : our company is a new start-up and so far the only material we have which include graphic design are our logo and our business cards (I did upload them on this website). This means that for us the way the bag will be design will give us a direction to follow for the print to come. For example if the bag are really "avant-garde" style, black and red, when we will do the stationary or the folders (with you maybe..) we won't do a very different style which would be for example green and yellow but will stick the "avant-garde" style, black and red (for example),... So doing those bags is also imagining what will be our corporate identity !
Updates
I forgot to give the dimensions for the bags :
2 bottles 70% recycled twisted handles 18 + 8 x39 cm
3 bottles timing integrated 26 + 8 x39 cm
Reason: I have only 3 designers who applied for he project. Thearen't bad but I really want to be able to choose among a few others as well.
Reason: Hello,
I just went through a major health issue this past month and couldn't work at all !
I am back on my feet now and really want to achieve the project...
Hello, I am really sorry I didn't post update for quite a while but I have been away for 3 weeks, due to some major health reasons, and couldn't work at all.
I am back on my feet now and really want this project to be successfull with your help.
Thank you very much for your understanding.
Mathis
Reason: Those are the last modifications.
A final decision will be made Friday on April 5th
Hello everybody,
Target Market(s)
between age 25 and 60 , well educated, god revenues, but accepting altrernative modes of living (like organic, environment friendly, clean energy etc.
Industry/Entity Type
Graphic Design
Requirements
Must have
- The name of the company : caveauxdoresclair.net
Our baseline : le goût sincère des vignes
Our address : 47 rue Fontenard - 75014 Paris - Tél. : 01 62 47 35 91
the phrase : Ouvert tous les jours jusque 22H *
* sauf le dimanche : 10h -14h (this in small)
All this text should be arrange and spreaded on different part of the bag in a way people do not feel it is a lot to read.
A good work and creativity in the use of a nice typeface would be appreciate
Nice to have
- I was thinking to ad a shape of a bottle (light and only suggested) ... why ?
Because our logo I like it, but the first image which come often to the public mind is to say : "it is a flower". If we say "it is also a glass of wine" ...they think at it and they finally say that yes it does also look like a glass of wine... but this isn't a spontaneous answer. So I feel important that the fact we sell wine ( I didn't say "the fact that we sell organic wine") has to be immediate for the people who look at the bag. And maybe adding or suggesting a modern, light and styled bottle of wine on the bag will help people understand that we indeed sell wine ? That just an idea of me, not a special request. So do as you think it is the best.
Should not have
- should not be to organic oriented as even if our name is "caveauxdoresclair.net" (which means "best organic wines") our clients clearly come more from the wine area than the organic area...
Should not find the inspiration on our website, since this website is an old one and we are completely renewing it...

```html
<!DOCTYPE html>
<html lang="fr">
<head>
<meta charset="utf-8">
<title>Caveaux Dorés Clair</title>
<link rel="stylesheet" href="https://fonts.googleapis.com/css2?family=Cormorant+Garamond:wght@600&family=Dancing+Script:wght@700&family=Arimo:ital,wght@0,400;1,700&display=swap">
<style>
  :root {
    --ink: #2a1a7a;
    --pink: #f29bc6;
    --pink-soft: #f8cfe2;
    --white: #ffffff;
    --cream: #fbf6a8;
    --wine: #b3182b;
  }
  * { margin: 0; padding: 0; box-sizing: border-box; }
  html, body { width: 1200px; height: 1061px; overflow: hidden; background: var(--white); }
  .bag-face {
    position: relative;
    width: 1200px;
    height: 1061px;
    overflow: hidden;
  }
  .backdrop {
    position: absolute;
    inset: 0;
    background: radial-gradient(ellipse at 680px 470px, var(--white) 0, var(--pink-soft) 55%, var(--pink) 100%);
  }
  .brand-dot {
    position: absolute;
    left: 150px;
    top: 230px;
    width: 150px;
    height: 150px;
    border-radius: 50%;
    background: var(--wine);
  }
  .brand-name {
    position: absolute;
    left: 340px;
    top: 190px;
    width: 720px;
    text-align: center;
    font-family: "Cormorant Garamond", serif;
    font-weight: 600;
    color: var(--ink);
    line-height: 1;
  }
  .brand-name .line-main { display: block; font-size: 170px; }
  .brand-name .line-sub { display: block; font-size: 72px; letter-spacing: 4px; margin-top: -6px; }
  .tagline {
    position: absolute;
    left: 340px;
    top: 500px;
    width: 720px;
    text-align: center;
    font-family: "Dancing Script", cursive;
    font-weight: 700;
    font-size: 50px;
    color: var(--ink);
  }
  .corner-panel {
    position: absolute;
    left: -120px;
    top: 755px;
    width: 404px;
    height: 420px;
    border-radius: 50%;
    background: var(--cream);
    box-shadow: 0 0 0 16px var(--white);
  }
  .shop-info {
    position: absolute;
    left: 45px;
    top: 958px;
    font-family: "Arimo", sans-serif;
    font-style: italic;
    font-weight: 700;
    font-size: 24px;
    line-height: 34px;
    color: var(--ink);
  }
  .shop-hours {
    position: absolute;
    left: 640px;
    top: 874px;
    width: 500px;
    text-align: center;
    font-family: "Arimo", sans-serif;
    font-style: normal;
    font-weight: 400;
    font-size: 19px;
    line-height: 27px;
    color: #111111;
  }
  .shop-hours .note { font-size: 15px; }
</style>
</head>
<body>
  <main class="bag-face">
    <div class="backdrop" role="img" aria-label="Fond décoratif en cercles roses et blancs"></div>
    <div class="brand-dot" aria-hidden="true"></div>
    <h1 class="brand-name">
      <span class="line-main">Caveaux</span>
      <span class="line-sub">DORÉS CLAIR</span>
    </h1>
    <p class="tagline">Le goût sincère des vignes</p>
    <div class="corner-panel" aria-hidden="true"></div>
    <address class="shop-info">
      Boutique 47 rue Fontenard - 75014 Paris<br>
      www.caveauxdoresclair.net
    </address>
    <p class="shop-hours">
      Tél. : 01 62 47 35 91<br>
      Ouvert tous les jours jusque 22H *<br>
      <span class="note">* sauf le dimanche : 10h - 14h</span>
    </p>
  </main>
</body>
</html>
```